Packaging Design Project

I need a box for a hair oil called NEL. 3 color, Simple design .. We are open to new ideas, the over all theme.. Pure and Simple , Natural, Color protect, good for the hair. We started with a basic design and this is the existing website http://nelhaircare.com/

Industry/Entity Type

Hair

```html
<!DOCTYPE html>
<html lang="en">
<head>
<meta charset="utf-8">
<title>NEL Hair Care – Hair Oil Box</title>
<link rel="stylesheet" href="https://fonts.googleapis.com/css2?family=Poiret+One&family=Tinos:wght@400;700&display=swap">
<style>
  :root {
    --board-red: #8c1c22;
    --board-red-deep: #6e1218;
    --fold-line: #3a0a0d;
    --label-black: #050505;
    --label-edge: #c9c9c9;
    --ink-white: #ffffff;
    --accent-red: #c3242b;
    --ink-black: #000000;
    --page: #ffffff;
  }
  * { box-sizing: border-box; margin: 0; padding: 0; }
  html, body { width: 1200px; height: 900px; overflow: hidden; background: var(--page); }
  .canvas { position: relative; width: 1200px; height: 900px; }

  .dieline { position: absolute; left: 0; top: 0; width: 1200px; height: 900px; }
  .dieline .board { fill: var(--board-red); stroke: var(--fold-line); stroke-width: 1; }
  .dieline .fold { stroke: var(--fold-line); stroke-width: 1; fill: none; }

  .label {
    position: absolute;
    background: var(--label-black);
    border: 2px solid var(--label-edge);
    border-radius: 22px;
    color: var(--ink-white);
    text-align: center;
  }
  .label-main { left: 389px; top: 221px; width: 165px; height: 392px; }
  .brand-mark {
    font-family: "Tinos", serif; font-weight: 700; color: var(--ink-white);
    line-height: 1.05;
  }
  .label-main .brand-mark { margin-top: 70px; font-size: 28px; }
  .brand-mark small { display: block; font-size: 0.38em; letter-spacing: 0.5px; }
  .product-name {
    font-family: "Poiret One", sans-serif; text-transform: uppercase;
    font-size: 11.5px; line-height: 1.3; letter-spacing: 0.3px;
  }
  .label-main .product-name { margin-top: 38px; }
  .claims {
    font-family: "Poiret One", sans-serif; color: var(--accent-red);
    font-size: 7px; line-height: 1.25;
  }
  .label-main .claims { margin-top: 24px; }
  .benefits {
    font-family: "Poiret One", sans-serif; font-size: 13px; line-height: 1.45;
  }
  .label-main .benefits { margin-top: 16px; }

  .net-volume {
    position: absolute; font-family: "Tinos", serif; font-weight: 700;
    color: var(--ink-white); white-space: nowrap;
  }
  .net-volume.on-dieline { left: 378px; width: 187px; top: 644px; text-align: center; font-size: 15px; }

  .origin-tag {
    position: absolute; background: var(--label-black);
    border: 1.5px solid var(--label-edge); border-radius: 5px;
    color: var(--ink-white); font-family: "Poiret One", sans-serif;
    display: flex; align-items: center; justify-content: center;
  }
  .origin-tag.on-dieline { left: 278px; top: 626px; width: 94px; height: 33px; font-size: 13px; }

  .info-tag {
    position: absolute; left: 572px; top: 228px; width: 93px; height: 52px;
    background: var(--label-black); border: 1.5px solid var(--label-edge);
    border-radius: 6px; text-align: center; padding-top: 7px;
    font-family: "Poiret One", sans-serif; font-size: 6.5px; line-height: 1.45;
  }
  .info-tag .lead { color: var(--accent-red); }
  .info-tag .web { color: var(--ink-white); }

  /* flat front panel */
  .front-panel {
    position: absolute; left: 905px; top: 72px; width: 150px; height: 465px;
    background: var(--board-red);
  }
  .front-panel .label { left: 13px; top: 14px; width: 124px; height: 390px; border-radius: 18px; }
  .front-panel .brand-mark { margin-top: 60px; font-size: 22px; }
  .front-panel .product-name { margin-top: 32px; font-size: 9.5px; }
  .front-panel .claims { margin-top: 20px; font-size: 5.5px; }
  .front-panel .benefits { margin-top: 12px; font-size: 11px; }
  .front-panel .net-volume { left: 0; width: 150px; top: 430px; text-align: center; font-size: 13px; }

  .brand-sheet {
    position: absolute; left: 730px; top: 605px; width: 395px; height: 235px;
    display: flex; flex-direction: column; align-items: center; justify-content: center;
    font-family: "Tinos", serif; font-weight: 700; color: var(--ink-black);
  }
  .brand-sheet .name { font-size: 64px; line-height: 1; letter-spacing: 2px; }
  .brand-sheet .sub { font-size: 28px; margin-top: 10px; }
</style>
</head>
<body>
<main class="canvas">

  <svg class="dieline" viewBox="0 0 1200 900" aria-label="Box dieline, flat">
    <!-- glue flap -->
    <path class="board" d="M30 222 L78 207 L78 672 L30 660 Z"/>
    <!-- back panel with bottom tab -->
    <path class="board" d="M78 207 H272 V672 H213 V712 Q213 720 205 720 H151 Q143 720 143 712 V672 H78 Z"/>
    <!-- left side panel with flaps -->
    <path class="board" d="M272 207 V180 L297 128 H378 V755 H297 L272 700 V672 Z"/>
    <!-- front panel with lid, tuck and bottom -->
    <path class="board" d="M378 128 V80 Q378 45 410 45 H533 Q565 45 565 80 V128 V755 V805 Q565 840 533 840 H410 Q378 840 378 805 V755 Z"/>
    <!-- right side panel with flaps -->
    <path class="board" d="M565 128 H645 L670 180 V207 V672 V700 L645 755 H565 Z"/>
    <line class="fold" x1="78" y1="207" x2="670" y2="207"/>
    <line class="fold" x1="78" y1="672" x2="670" y2="672"/>
    <line class="fold" x1="378" y1="128" x2="565" y2="128"/>
    <line class="fold" x1="378" y1="755" x2="565" y2="755"/>
    <line class="fold" x1="272" y1="207" x2="272" y2="672"/>
    <line class="fold" x1="378" y1="128" x2="378" y2="755"/>
    <line class="fold" x1="565" y1="128" x2="565" y2="755"/>
  </svg>

  <section class="label label-main">
    <div class="brand-mark">NEL<small>HAIR CARE</small></div>
    <p class="product-name">Protective hair-oil<br>treatment<br>and styling aid</p>
    <p class="claims">paraben free - sulfate free<br>alergy tested - alcohol free</p>
    <p class="benefits">style, smooth<br>shine &amp; condition<br>ALL hair types<br>while locking in<br>moisture</p>
  </section>
  <p class="net-volume on-dieline">100ml / 3.4 oz</p>
  <div class="origin-tag on-dieline">Made in USA</div>
  <div class="info-tag">
    <p class="lead">For more information<br>visit us online at</p>
    <p class="web">www.nelhaircare.com</p>
  </div>

  <section class="front-panel">
    <div class="label">
      <div class="brand-mark">NEL<small>HAIR CARE</small></div>
      <p class="product-name">Protective hair-oil<br>treatment<br>and styling aid</p>
      <p class="claims">paraben free - sulfate free<br>alergy tested - alcohol free</p>
      <p class="benefits">style, smooth<br>shine &amp; condition<br>ALL hair types<br>while locking in<br>moisture</p>
    </div>
    <p class="net-volume">100ml / 3.4 oz</p>
  </section>

  <section class="brand-sheet">
    <span class="name">NEL</span>
    <span class="sub">HAIR CARE</span>
  </section>

</main>
</body>
</html>
```